Web Design Project

Hi, we need a new and professional design for our company "partnertradingcircuit". The website should communicate business but with a friendly and professional touch.

You can use the following categories for the menu;

Home - customer groups - products - voucher system- contact

Give it your best,

Regards,
Anselm

Industry/Entity Type

Business

```html
<!DOCTYPE html>
<html lang="en">
<head>
<meta charset="utf-8">
<title>partnertradingcircuit</title>
<link rel="stylesheet" href="https://fonts.googleapis.com/css2?family=Roboto+Condensed:wght@300;400;700&family=Arimo:wght@400;700&display=swap">
<style>
:root{
  --page:#e3e1d9;
  --panel:#ffffff;
  --ink:#3b3b3b;
  --ink-soft:#6e6e6e;
  --body-text:#444444;
  --link:#1561b3;
  --accent:#1f87d6;
  --blue-band:#0a5bbf;
  --wood-light:#f3e3c6;
  --wood-dark:#c9a57a;
  --hero-tan:#dcc4a5;
  --hero-green:#c2cda6;
  --nav-bg:#f1f0ec;
  --nav-edge:#d6d4cc;
  --contact-bg:#c8bf95;
  --rule:#b9b9b9;
}
*{margin:0;padding:0;box-sizing:border-box}
html,body{width:1200px;height:1128px;overflow:hidden}
body{background:var(--page);font-family:"Arimo",Arial,sans-serif;color:var(--ink);position:relative}
.abs{position:absolute}
.datebar{left:86px;top:70px;font-size:14px;color:#555}
.datebar b{font-weight:700}
.datebar .time{margin-left:14px;font-weight:700;font-size:15px}
.panel{left:345px;top:34px;width:836px;height:1022px;background:var(--panel);border-radius:10px;box-shadow:0 2px 8px rgba(0,0,0,.18)}
.toolbar{left:396px;top:66px;display:flex;align-items:center}
.toolbar .tool{width:22px;height:22px;display:flex;align-items:center;justify-content:center}
.toolbar .sep{width:1px;height:26px;background:#cfcfcf;margin:0 34px}
.banner{left:19px;top:114px;width:1162px;height:188px;background:linear-gradient(180deg,var(--wood-light),var(--wood-dark));box-shadow:0 3px 6px rgba(0,0,0,.25)}
.banner-photo{left:345px;top:114px;width:480px;height:188px;background:linear-gradient(90deg,var(--hero-tan) 0%,var(--hero-green) 50%,var(--hero-tan) 100%)}
.brand{left:36px;top:172px;font-family:"Arimo",Arial,sans-serif;font-weight:700;font-size:30px;color:#1a7fc8}
.slogan{left:736px;top:154px;width:445px;height:104px;background:var(--blue-band);border-radius:6px 0 0 6px;color:#fff;font-family:"Roboto Condensed",Arial,sans-serif;padding:18px 0 0 26px}
.slogan .big{font-size:41px;font-weight:400;line-height:1;letter-spacing:1px}
.slogan .small{font-size:24px;font-weight:300;line-height:1.2}
.pin{left:1124px;top:139px;width:32px;height:32px;border-radius:50%;background:#fff;border:2px solid #cfcfcf}
.nav{left:34px;top:310px;width:311px;list-style:none}
.nav li{height:80px;margin-bottom:8px;background:var(--nav-bg);border:1px solid var(--nav-edge);border-right:none;border-radius:6px 0 0 6px;padding:19px 0 0 31px}
.nav .title{font-family:"Roboto Condensed",Arial,sans-serif;font-size:22px;color:#333;line-height:1.1}
.nav .sub{font-family:"Roboto Condensed",Arial,sans-serif;font-size:16px;color:#7b7b7b;line-height:1}
.contact{left:34px;top:851px;width:311px;height:155px;background:var(--contact-bg);border-radius:8px 0 0 8px;padding:14px 0 0 46px;color:#4a4535;font-size:16px;line-height:1.3}
.contact h3{font-family:"Roboto Condensed",Arial,sans-serif;font-weight:400;font-size:26px;color:#4a4535;margin-bottom:6px}
.contact .name{font-weight:700}
.photo{border-radius:8px;border:1px solid #9e9e9e}
h2{font-family:"Roboto Condensed",Arial,sans-serif;font-weight:700;font-size:31px;color:#3a3a3a;letter-spacing:-.6px;line-height:1.05}
.subhead{font-family:"Roboto Condensed",Arial,sans-serif;font-size:18px;color:#777;line-height:1.1}
.text{font-size:16.5px;line-height:21px;color:var(--body-text)}
.more{font-size:16px;color:var(--link)}
.more::before{content:"| ";color:#999}
.more::after{content:" |";color:#999}
.more span{color:#999;font-size:11px;margin-right:3px}
.rule{height:1px;background:var(--rule)}
.links{list-style:none;left:393px;top:842px;width:335px}
.links li{height:28px;border-bottom:1px dotted #9a9a9a;font-size:16.5px;color:var(--link);padding:4px 0 0 16px;position:relative}
.links li::before{content:"";position:absolute;left:2px;top:12px;width:5px;height:5px;border:1px solid #8aa;border-radius:50%}
.news-date{color:var(--accent);font-weight:700;font-size:19px}
.footer{left:0;top:1071px;width:1349px;text-align:center;font-size:16px;color:#444}
</style>
</head>
<body>
<div class="abs datebar"><b>FRI</b> 00.00.2013 <span class="time">5:45</span> PM</div>

<div class="abs panel"></div>

<div class="abs toolbar">
  <div class="tool"><svg width="18" height="16" viewBox="0 0 18 16"><path d="M2 8 9 2l7 6M4 7v7h4v-4h2v4h4V7" fill="none" stroke="#666" stroke-width="1.4"/></svg></div>
  <div class="sep"></div>
  <div class="tool"><svg width="14" height="17" viewBox="0 0 14 17"><path d="M2 1h7l3 3v12H2z" fill="none" stroke="#666" stroke-width="1.4"/></svg></div>
  <div class="sep"></div>
  <div class="tool"><svg width="18" height="17" viewBox="0 0 18 17"><path d="M6 1h6v4H6zM1 12h6v4H1zM11 12h6v4h-6zM9 5v4M4 12V9h10v3" fill="none" stroke="#666" stroke-width="1.4"/></svg></div>
</div>

<div class="abs banner"></div>
<div class="abs banner-photo" role="img" aria-label="Header photograph: hands holding a globe"></div>
<div class="abs brand">partnertradingcircuit</div>
<div class="abs slogan"><div class="big">INDIVIDUAL</div><div class="small">CUSTOMERS APPROACH</div></div>
<div class="abs pin"></div>

<ul class="abs nav">
  <li><div class="title">Home</div><div class="sub">lorem empus</div></li>
  <li><div class="title">Customer Groups</div><div class="sub">lorem epsum</div></li>
  <li><div class="title">Products</div><div class="sub">lorum epsum</div></li>
  <li><div class="title">Voucher System</div><div class="sub">lerum epsum</div></li>
  <li><div class="title">Contact</div><div class="sub">lerum epsum</div></li>
</ul>

<div class="abs contact">
  <h3>Primary Contact</h3>
  <div class="name">The Company Name Inc.</div>
  <div>4410 - 4418 Kestrel Lane,</div>
  <div>London, KT04 2QR</div>
  <div><b>Phone:</b> &nbsp;+1 800 555 0142</div>
</div>

<div class="abs photo" style="left:393px;top:382px;width:208px;height:174px;background:linear-gradient(135deg,#e9e4dc,#c9b9a3 55%,#f4f1ec)" role="img" aria-label="Portrait of a businesswoman in a light blouse"></div>
<h2 class="abs" style="left:631px;top:377px">Welcome to our Company Website</h2>
<div class="abs subhead" style="left:633px;top:409px">Some words about company</div>
<p class="abs text" style="left:631px;top:453px;width:500px">Donec et tortor. Praesent iaculis vestibulum neque arcu tortor... fringilla ut, suscipit ac, condimentum sit amet, est. Praesent malesuada purus at dolor. Maecenas porttitor, ante nec pulvinar suscipit, ante nisl lobortis dui, eu malesuada pede tortor mollis wisi. Suspendisse egestas. Quisque enim...</p>
<div class="abs more" style="right:68px;top:565px"><span>+</span>read more about company</div>

<h2 class="abs" style="left:393px;top:629px">Priority line of business</h2>
<div class="abs subhead" style="left:393px;top:660px">Professional management and researches</div>
<div class="abs rule" style="left:393px;top:691px;width:335px"></div>
<p class="abs text" style="left:393px;top:722px;width:335px">Praesent malesuada purus at dolor. Suspendisse egestas. Quisque enim. Duis neque pede, ultrices sed, vulputate at, vestibulum id, nunc quisque orci quam, consectetuer quis, rhoncus sed...</p>
<ul class="abs links">
  <li>Praesent malesuada purus at dolor.</li>
  <li>Suspendisse egestas quisque enim.</li>
  <li>Duis neque pede ultrices sed vulput</li>
  <li>Quisque orci quam, consectetuer quis</li>
  <li>Rhoncus sed vehicula nec velit.</li>
</ul>

<div class="abs" style="left:761px;top:616px;width:1px;height:366px;background:#bdbdbd"></div>

<h2 class="abs" style="left:794px;top:629px">Latest News</h2>
<div class="abs subhead" style="left:794px;top:660px">corporate highlights</div>

<div class="abs photo" style="left:794px;top:727px;width:129px;height:88px;background:linear-gradient(135deg,#3a3a3a,#8b7a6a 50%,#d8cfc4)" role="img" aria-label="Smiling woman at an office desk"></div>
<p class="abs text" style="left:945px;top:723px;width:190px"><span class="news-date">21.05</span>&nbsp; Praesent iaculis vestibulum neque arcu tortor fringilla ut, suscipit ac, condimentum sit...</p>
<div class="abs more" style="right:68px;top:815px"><span>+</span>read more</div>
<div class="abs" style="left:794px;top:866px;width:337px;border-top:1px dotted #9a9a9a"></div>

<div class="abs photo" style="left:794px;top:882px;width:129px;height:88px;background:linear-gradient(135deg,#cfd9e2,#8fa4b6 50%,#e7e2dc)" role="img" aria-label="Smiling woman talking on a phone"></div>
<p class="abs text" style="left:945px;top:879px;width:190px"><span class="news-date">15.05</span>&nbsp; Praesent male-suada purus at dolor. Maecenas porttitor, ante nec pulvinar suscipit...</p>
<div class="abs more" style="right:68px;top:970px"><span>+</span>read more</div>

<div class="abs footer">partnertradingcircuit.Com © 2013 | Privacy Policy | Terms Of Use</div>
</body>
</html>
```